HYPNO Business Card

provide hypnotherapy and counselling for addictions, weight loss, anxiety, depression, smoking, alcohol etc
i would like the design to fit in with a feeling of peace and tranquility

Industry/Entity Type

Hypnotherapy

Contact Information for Business Card

Lena Castrell
Clinical Hypnotherapist and Counsellor
BA Social Work
Dip Clinical Hypnotherapy and Psychotherapy

Phone: 0438175203
Email: abluegatehypnotherapy@quillbox.net

```html
<!DOCTYPE html>
<html lang="en">
<head>
<meta charset="utf-8">
<title>Lena Castrell – Business Card</title>
<link rel="stylesheet" href="https://fonts.googleapis.com/css2?family=Arimo:wght@400;500&display=swap">
<style>
  :root {
    --page-bg: #e9e6e0;
    --card-white: #ffffff;
    --sun-yellow: #f6ec34;
    --sun-yellow-deep: #ebe02a;
    --leaf-light: #cfe27c;
    --leaf: #93bd35;
    --band-black: #0b0b0b;
    --ink: #151515;
    --placeholder-grey: #d6d8dc;
  }
  * { margin: 0; padding: 0; box-sizing: border-box; }
  html, body {
    width: 1200px;
    height: 818px;
    overflow: hidden;
    background: var(--page-bg);
  }
  .business-card {
    position: absolute;
    left: 130px;
    top: 124px;
    width: 940px;
    height: 570px;
    background: var(--card-white);
    box-shadow: 0 10px 30px rgba(0,0,0,0.18);
    overflow: hidden;
    font-family: "Arimo", Arial, sans-serif;
    color: var(--ink);
  }
  .card-shapes {
    position: absolute;
    inset: 0;
    width: 100%;
    height: 100%;
  }
  .identity {
    position: absolute;
    right: 92px;
    top: 58px;
    text-align: right;
  }
  .identity__name {
    font-size: 40px;
    font-weight: 500;
    letter-spacing: 0.5px;
    line-height: 1.1;
  }
  .identity__role {
    margin-top: 10px;
    font-size: 20px;
    font-weight: 400;
  }
  .identity__credentials {
    margin-top: 4px;
    font-size: 17px;
    font-weight: 400;
  }
  .contact {
    position: absolute;
    right: 40px;
    top: 372px;
    list-style: none;
    text-align: right;
  }
  .contact__item {
    display: flex;
    justify-content: flex-end;
    align-items: center;
    gap: 22px;
    font-size: 22px;
    line-height: 1;
    margin-bottom: 38px;
  }
  .contact__icon {
    width: 22px;
    height: 22px;
    flex: none;
  }
</style>
</head>
<body>
  <main class="business-card">
    <svg class="card-shapes" viewBox="0 0 940 570" aria-hidden="true">
      <defs>
        <linearGradient id="leafGradient" x1="0" y1="0" x2="1" y2="0.3">
          <stop offset="0" stop-color="var(--leaf-light)"/>
          <stop offset="1" stop-color="var(--leaf)"/>
        </linearGradient>
        <linearGradient id="sunGradient" x1="0" y1="0" x2="1" y2="1">
          <stop offset="0" stop-color="var(--sun-yellow)"/>
          <stop offset="1" stop-color="var(--sun-yellow-deep)"/>
        </linearGradient>
      </defs>
      <path class="leaf-field" d="M120,570 C300,480 400,380 470,260 L940,230 V570 Z" fill="url(#leafGradient)"/>
      <path class="swoosh-band" d="M226,0 H940 V325 C840,358 700,385 590,362 C470,334 370,250 300,160 Z" fill="var(--band-black)"/>
      <path class="sun-field" d="M226,0 H940 V262 C840,300 700,332 600,302 C470,262 330,150 226,0 Z" fill="url(#sunGradient)"/>
      <circle class="association-badge" cx="180" cy="330" r="88" fill="var(--placeholder-grey)"/>
      <rect class="register-listing" x="100" y="446" width="120" height="44" fill="var(--placeholder-grey)"/>
    </svg>

    <header class="identity">
      <h1 class="identity__name">Lena Castrell</h1>
      <p class="identity__role">Clinical Hypnotherapist and Counsellor</p>
      <p class="identity__credentials">BA Social Work Dip Clinical Hypnotherapy and Psychotherapy</p>
    </header>

    <ul class="contact">
      <li class="contact__item contact__item--phone">
        <span>0438175203</span>
        <svg class="contact__icon" viewBox="0 0 24 24" aria-label="Phone">
          <path d="M6.6 10.8c1.4 2.8 3.8 5.1 6.6 6.6l2.2-2.2c.3-.3.7-.4 1-.2 1.1.4 2.3.6 3.6.6.6 0 1 .4 1 1V20c0 .6-.4 1-1 1C10.6 21 3 13.4 3 4c0-.6.4-1 1-1h3.5c.6 0 1 .4 1 1 0 1.3.2 2.5.6 3.6.1.3 0 .7-.2 1z" fill="var(--ink)"/>
        </svg>
      </li>
      <li class="contact__item contact__item--email">
        <span>abluegatehypnotherapy@quillbox.net</span>
        <svg class="contact__icon" viewBox="0 0 24 24" aria-label="Email">
          <rect x="2" y="5" width="20" height="14" fill="var(--ink)"/>
          <path d="M2.5 5.5 L12 13 L21.5 5.5" fill="none" stroke="var(--leaf-light)" stroke-width="1.6"/>
        </svg>
      </li>
    </ul>
  </main>
</body>
</html>
```